Election features for a political website

The Hearthside Ledger (www.hearthsideledger.example)
Web banner designs
Please have a look at The Hearthside Ledger website (www.hearthsideledger.example). We are seeking to add an advertising style banner at the top of every page and post. It will run right across the page (1024 pixels) and be in the region of 200 pixels vertically. (Please advise on what looks best size wise.
The banner will be a slider, operated in a similar way to the current homepage slider. There will be four items on the slider, and so we need four designs that match the aesthetic feel of the website. Each slider will link through to posts on the website.
1.
Headline: OUR CANDIDATE OF THE DAY
Space for a name, head and shoulders picture of the person to be dropped in and a one line reason. This will need to be in an editable format as this image will be changed each day for one month.
2.
Headline: HERO OF THE DAY
Space for name and a one line reason. This will need to be in an editable format as this image will be changed each day for one month.
3.
Headline: VILLAIN OF THE DAY
Space for name of the person to be dropped in and a one line reason. This will need to be in an editable format as this image will be changed each day for one month.
4.
Headline: THL Poll – [Date]
If the election was today, who would you vote for?
Clickable options:
Brightfolders
Ashvel
Marden Alliancers
Vornu
Tally
Other
Can a poll widget be added to the banner? We would like this poll to reset each day and then pool the results into a graph day by day over a one month period.
Reason: Payment is now guaranteed. We would like to see more options.

```html
<!DOCTYPE html>
<html lang="en">
<head>
<meta charset="utf-8">
<title>Hero of the Day – The Hearthside Ledger</title>
<link href="https://fonts.googleapis.com/css2?family=Oswald:wght@400;700&family=Raleway:wght@400&family=Fira+Sans+Condensed:wght@700&family=Fira+Sans:wght@400;700&display=swap" rel="stylesheet">
<style>
  :root {
    --ink: #1c1c1c;
    --brand-blue: #0d5288;
    --text-blue: #13558a;
    --banner-light: #e6e6e6;
    --nav-bg: rgba(38, 38, 38, 0.82);
    --nav-text: #ffffff;
    --search-text: #b9b9b9;
    --headline-bg: rgba(30, 30, 30, 0.42);
    --white: #ffffff;
  }
  * { margin: 0; padding: 0; box-sizing: border-box; }
  html, body { width: 1200px; height: 730px; overflow: hidden; background: var(--white); }
  .canvas { position: relative; width: 1200px; height: 730px; overflow: hidden; font-family: "Fira Sans", sans-serif; }

  /* Hero banner */
  .hero-banner {
    position: absolute; left: 0; top: 0; width: 1200px; height: 198px;
    background: linear-gradient(90deg, #cdcdcd 0%, var(--banner-light) 22%, #ededed 50%, var(--banner-light) 78%, #cbcbcb 100%);
  }
  .banner-backdrop { position: absolute; top: 0; height: 198px; }
  .banner-backdrop--left { left: 0; width: 260px; background: linear-gradient(90deg, #c4c4c4, rgba(230,230,230,0)); }
  .banner-backdrop--right { right: 0; width: 220px; background: linear-gradient(270deg, #c6c6c6, rgba(230,230,230,0)); }

  .hero-title { position: absolute; left: 180px; top: 38px; font-family: "Oswald", sans-serif; font-weight: 700; }
  .hero-title__main { display: block; font-weight: 700; font-size: 78px; line-height: 78px; color: var(--ink); letter-spacing: -2px; transform: scaleX(0.9); transform-origin: left center; }
  .hero-title__sub { display: block; margin-left: 38px; font-weight: 400; font-size: 33px; line-height: 36px; color: var(--text-blue); }

  .hero-portrait {
    position: absolute; left: 431px; top: 23px; width: 150px; height: 150px; border-radius: 50%;
    border: 4px solid var(--white); box-shadow: 0 0 0 1px #bdbdbd;
    background: linear-gradient(180deg, #d9d9d9 0%, #b08468 35%, #7a5a45 70%, #2f3a44 100%);
  }
  .hero-name { position: absolute; left: 603px; top: 57px; font-family: "Oswald", sans-serif; font-weight: 400; font-size: 32px; line-height: 42px; color: var(--text-blue); }
  .hero-reason { position: absolute; left: 597px; top: 106px; font-family: "Raleway", sans-serif; font-size: 15.8px; color: var(--ink); }

  /* Feature slider */
  .site-feature {
    position: absolute; left: 0; top: 198px; width: 1200px; height: 532px;
    background:
      radial-gradient(ellipse 300px 220px at 900px 120px, rgba(215,215,215,0.75), rgba(215,215,215,0) 70%),
      radial-gradient(ellipse 260px 200px at 620px 90px, rgba(200,200,200,0.6), rgba(200,200,200,0) 70%),
      radial-gradient(ellipse 220px 300px at 80px 320px, rgba(35,35,35,0.8), rgba(35,35,35,0) 70%),
      radial-gradient(ellipse 260px 260px at 1080px 360px, rgba(225,225,225,0.55), rgba(225,225,225,0) 70%),
      radial-gradient(ellipse 300px 180px at 850px 470px, rgba(40,40,40,0.7), rgba(40,40,40,0) 70%),
      radial-gradient(ellipse 200px 220px at 530px 260px, rgba(230,230,230,0.5), rgba(230,230,230,0) 70%),
      linear-gradient(180deg, #a9a9a9 0%, #8d8d8d 40%, #5e5e5e 75%, #3c3c3c 100%);
  }
  .site-nav {
    position: absolute; left: 0; top: 0; width: 1200px; height: 38px; background: var(--nav-bg);
    display: flex; align-items: center; padding-left: 551px;
  }
  .site-nav__link { font-family: "Fira Sans Condensed", sans-serif; font-weight: 700; font-size: 13px; color: var(--nav-text); margin-right: 14px; text-decoration: none; }
  .site-nav__search { font-family: "Fira Sans", sans-serif; font-size: 12px; color: var(--search-text); margin-left: 2px; }

  .site-brand { position: absolute; left: 118px; top: 34px; display: flex; align-items: center; gap: 16px; }
  .site-brand__mark { width: 30px; height: 30px; background: var(--brand-blue); }
  .site-brand__name { font-family: "Fira Sans", sans-serif; font-weight: 700; font-size: 40px; color: var(--white); line-height: 1; }

  .feature-headline {
    position: absolute; left: 118px; top: 282px; width: 708px; height: 192px; background: var(--headline-bg);
    padding: 6px 20px;
  }
  .feature-headline__text { width: 630px; font-family: "Fira Sans", sans-serif; font-weight: 700; font-size: 36px; line-height: 46px; color: var(--white); }

  .slider-arrows { position: absolute; left: 163px; top: 506px; }
</style>
</head>
<body>
<div class="canvas">
  <section class="hero-banner">
    <div class="banner-backdrop banner-backdrop--left" role="img" aria-label="Faded black-and-white photo of a smiling woman"></div>
    <div class="banner-backdrop banner-backdrop--right" role="img" aria-label="Faded black-and-white photo of a laughing woman"></div>

    <h1 class="hero-title">
      <span class="hero-title__main">HERO</span>
      <span class="hero-title__sub">OF THE DAY</span>
    </h1>
    <div class="hero-portrait" role="img" aria-label="Head and shoulders portrait of today's hero"></div>
    <h2 class="hero-name">John Smith</h2>
    <p class="hero-reason">“ Lorem ipsum dolor sit amet consectetur adipisicing elit ”</p>
  </section>

  <section class="site-feature" role="img" aria-label="Black-and-white photo of musicians and dancers at an outdoor gathering under trees">
    <nav class="site-nav">
      <a class="site-nav__link">Our mission</a>
      <a class="site-nav__link">Write for us</a>
      <a class="site-nav__link">About</a>
      <a class="site-nav__link">Donate</a>
      <a class="site-nav__link">Sign up</a>
      <a class="site-nav__link">Contact</a>
      <span class="site-nav__search">Search Hearthside Ledger</span>
    </nav>

    <div class="site-brand">
      <span class="site-brand__mark"></span>
      <span class="site-brand__name">The Hearthside Ledger</span>
    </div>

    <div class="feature-headline">
      <p class="feature-headline__text">Maren Holloway: Spare a thought for the hippies. Their free love revolution is now regulated by a state clipboard</p>
    </div>

    <svg class="slider-arrows" width="80" height="16" viewBox="0 0 80 16" aria-label="Previous and next slide">
      <g fill="none" stroke="#ffffff" stroke-width="1.6" stroke-linecap="round">
        <path d="M2 8 H36 M2 8 L9 2 M2 8 L9 14"/>
        <path d="M42 8 H77 M77 8 L70 2 M77 8 L70 14"/>
      </g>
    </svg>
  </section>
</div>
</body>
</html>
```